Paper Lighthouse Book Cover

Copper Wren Publishers is looking for a book cover suitable for their new release "The Paper Lighthouse". A modern detective story set in Los Angeles with a science fiction overlay. The book is the first of a series, and subsequent editions will need covers which match the first. The back cover text summarizes the plot.

Must deliver files suitable for Adobe Illustrator, matching the included cover template.

Target Market(s)

People who like science fiction and noir detective stories

Font styles to use
Serif

```html
<!DOCTYPE html>
<html lang="en">
<head>
<meta charset="utf-8">
<title>The Paper Lighthouse — Cover</title>
<link rel="stylesheet" href="https://fonts.googleapis.com/css2?family=Playfair+Display:wght@700;900&display=swap">
<style>
  :root {
    --backdrop: #e3e3e3;
    --night: #06061a;
    --deep-blue: #101048;
    --electric: #3a5cff;
    --glow: #b7c6ff;
    --cyan: #1aa6e0;
    --white: #ffffff;
  }
  html, body {
    margin: 0;
    width: 1015px;
    height: 1200px;
    overflow: hidden;
    background: var(--backdrop);
  }
  .cover {
    position: absolute;
    left: 147px;
    top: 60px;
    width: 720px;
    height: 1080px;
    overflow: hidden;
    background: var(--night);
    box-shadow: 0 10px 30px rgba(0,0,0,0.25);
  }
  .cover-art {
    position: absolute;
    inset: 0;
    background:
      radial-gradient(ellipse 18% 14% at 58% 66%, rgba(215,225,255,0.75), rgba(90,120,255,0.45) 45%, transparent 80%),
      radial-gradient(ellipse 30% 22% at 62% 72%, rgba(58,92,255,0.45), transparent 80%),
      radial-gradient(ellipse 35% 16% at 40% 8%, rgba(150,170,255,0.7), rgba(58,92,255,0.3) 50%, transparent 80%),
      linear-gradient(100deg, transparent 48%, rgba(160,180,255,0.35) 53%, rgba(230,236,255,0.55) 55%, rgba(160,180,255,0.35) 57%, transparent 62%),
      radial-gradient(ellipse 45% 30% at 82% 88%, rgba(40,60,210,0.5), transparent 80%),
      radial-gradient(ellipse 22% 40% at 20% 55%, rgba(120,130,170,0.18), transparent 80%),
      radial-gradient(ellipse 18% 35% at 85% 40%, rgba(120,130,170,0.15), transparent 80%),
      linear-gradient(180deg, var(--deep-blue) 0%, var(--night) 45%, #0b0b2e 100%);
  }
  .title {
    position: absolute;
    left: 50px;
    top: 150px;
    width: 640px;
    margin: 0;
    transform: rotate(-13deg);
    transform-origin: center;
    font-family: "Playfair Display", "Georgia", serif;
    font-weight: 900;
    line-height: 0.92;
    text-transform: uppercase;
  }
  .title-article {
    display: block;
    font-size: 54px;
    color: var(--cyan);
    margin-left: 20px;
  }
  .title-word {
    display: block;
    color: var(--white);
    -webkit-text-stroke: 6px var(--cyan);
    paint-order: stroke fill;
    text-shadow: 0 0 16px rgba(26,166,224,0.6);
  }
  .title-word.first {
    font-size: 110px;
    margin-left: 40px;
  }
  .title-word.second {
    font-size: 80px;
    margin-left: 10px;
  }
  .author {
    position: absolute;
    right: 90px;
    bottom: 120px;
    margin: 0;
    transform: rotate(-13deg);
    font-family: "Playfair Display", "Georgia", serif;
    font-weight: 700;
    font-size: 64px;
    letter-spacing: 2px;
    color: var(--white);
    text-shadow: 0 0 12px rgba(183,198,255,0.7);
  }
</style>
</head>
<body>
  <main class="cover">
    <div class="cover-art" role="img" aria-label="Cover illustration: a silhouetted detective in a fedora and trench coat on a blurred night city street, wrapped in crackling blue lightning"></div>
    <h1 class="title">
      <span class="title-article">The</span>
      <span class="title-word first">Paper</span>
      <span class="title-word second">Lighthouse</span>
    </h1>
    <p class="author">R. T. VALE</p>
  </main>
</body>
</html>
```